Twitter optimized logo and banner design

I would like to have a customized set of graphics for both the logo and header for our Twitter page. (I'm attaching our logo in EPS format.) We are a payroll service that provides payroll, HR help desk, benefits administration and web time clocks to our clients. Please see our website at www.corvanpay.net. Thank you!

Target Market(s)

All interested prospects

Industry/Entity Type

It Service

Font styles to use
Sans Serif

Requirements
Must have
• Common color scheme which makes the logo and head work together.
Should not have
• Too much text

```html
<!DOCTYPE html>
<html lang="en">
<head>
<meta charset="utf-8">
<title>Corvan Pay Solutions – Social Banners</title>
<link rel="stylesheet" href="https://fonts.googleapis.com/css2?family=Ubuntu:wght@500;700&family=Poppins:ital,wght@0,400;0,700;1,300&display=swap">
<style>
  :root {
    --brand-blue: #12aee8;
    --brand-blue-soft: #dcf0fb;
    --ink: #111111;
    --white: #ffffff;
    --photo-cool-a: #c9dcea;
    --photo-cool-b: #7fa3c2;
    --photo-light-a: #f4f6f8;
    --photo-light-b: #d6dde3;
  }
  * { margin: 0; padding: 0; box-sizing: border-box; }
  html, body { width: 1200px; height: 1046px; overflow: hidden; background: var(--white); }
  .canvas { position: relative; width: 1200px; height: 1046px; }
  .banner { position: absolute; left: 0; width: 1200px; height: 523px; }
  .banner--team { top: 0; }
  .banner--office { top: 523px; }
  .banner__photo { position: absolute; left: 0; top: 0; width: 1200px; height: 400px; }
  .banner--team .banner__photo { background: linear-gradient(110deg, var(--photo-cool-a) 0%, #a9c3d8 45%, var(--photo-cool-b) 100%); }
  .banner--office .banner__photo { background: linear-gradient(110deg, var(--photo-light-a) 0%, var(--photo-light-b) 60%, #b9c6d2 100%); }
  .service-tag {
    position: absolute; height: 72px; background: var(--brand-blue); color: var(--white);
    font-family: "Ubuntu", sans-serif; font-weight: 500; font-size: 39px; line-height: 72px;
    letter-spacing: 0.5px; white-space: nowrap;
  }
  .service-tag--payroll { left: 0; top: 0; width: 414px; padding-left: 40px; }
  .service-tag--helpdesk { left: 0; top: 80px; width: 330px; padding-left: 40px; }
  .service-tag--timeclock { left: 800px; top: 0; width: 400px; padding-left: 40px; }
  .service-tag--peo { left: 1050px; top: 80px; width: 150px; padding-left: 40px; }
  .brand-tile {
    position: absolute; left: 118px; top: 283px; width: 211px; height: 211px; border-radius: 9px;
    background: var(--brand-blue); color: var(--white); display: flex; align-items: center; justify-content: center;
    font-family: "Poppins", sans-serif; font-weight: 700; font-size: 40px;
  }
  .tagline-strip {
    position: absolute; left: 352px; top: 360px; width: 505px; height: 40px;
    background: rgba(255,255,255,0.55);
  }
  .tagline-rule { position: absolute; left: 352px; top: 360px; width: 826px; height: 1.5px; background: var(--ink); }
  .tagline {
    position: absolute; left: 367px; top: 366px; font-family: "Poppins", sans-serif; font-style: italic;
    font-weight: 300; font-size: 20.5px; color: var(--ink); white-space: nowrap;
  }
  .signature-panel { position: absolute; left: 900px; top: 283px; width: 300px; height: 117px; background: rgba(255,255,255,0.72); }
  .signature-url {
    position: absolute; left: 948px; top: 288px; font-family: "Poppins", sans-serif; font-size: 18px; color: var(--ink);
  }
  .signature-name {
    position: absolute; left: 940px; top: 312px; width: 220px; text-align: center;
    font-family: "Poppins", sans-serif; font-weight: 700; font-size: 40px; letter-spacing: 3px; color: var(--ink); line-height: 48px;
  }
  .signature-sub {
    position: absolute; left: 940px; top: 362px; width: 225px; text-align: center;
    font-family: "Poppins", sans-serif; font-weight: 700; font-size: 22px; color: var(--ink);
  }
  .accent-dot { position: absolute; left: 1062px; top: 406px; width: 100px; height: 100px; border-radius: 50%; background: var(--brand-blue-soft); }
</style>
</head>
<body>
<main class="canvas">
  <section class="banner banner--team">
    <div class="banner__photo" role="img" aria-label="Photo of three colleagues smiling at a laptop in a bright office"></div>
    <div class="service-tag service-tag--payroll">PAYROLL SERVICE</div>
    <div class="service-tag service-tag--helpdesk">HR HELP DESK</div>
    <div class="service-tag service-tag--timeclock">WEB TIME CLOCK</div>
    <div class="service-tag service-tag--peo">PEO</div>
    <div class="tagline-strip"></div>
    <div class="tagline-rule"></div>
    <p class="tagline">We Provide Answers to Your Business Problems</p>
    <div class="signature-panel"></div>
    <p class="signature-url">www.corvanpay.net</p>
    <p class="signature-name">CORVAN</p>
    <p class="signature-sub">PAY SOLUTIONS</p>
    <div class="brand-tile">Corvan</div>
    <div class="accent-dot"></div>
  </section>

  <section class="banner banner--office">
    <div class="banner__photo" role="img" aria-label="Photo of four business people posing around a meeting table with a laptop"></div>
    <div class="service-tag service-tag--payroll">PAYROLL SERVICE</div>
    <div class="service-tag service-tag--helpdesk">HR HELP DESK</div>
    <div class="service-tag service-tag--timeclock">WEB TIME CLOCK</div>
    <div class="service-tag service-tag--peo">PEO</div>
    <div class="tagline-strip"></div>
    <div class="tagline-rule"></div>
    <p class="tagline">We Provide Answers to Your Business Problems</p>
    <div class="signature-panel"></div>
    <p class="signature-url">www.corvanpay.net</p>
    <p class="signature-name">CORVAN</p>
    <p class="signature-sub">PAY SOLUTIONS</p>
    <div class="brand-tile">Corvan</div>
    <div class="accent-dot"></div>
  </section>
</main>
</body>
</html>
```